Wavelume artwork for new single release

I need Wavelume artwork creating to release a new single on there.

The specs are:

Ideal size: 3000 x 3000 pixels
Minimum size: 1400 x 1400 pixels
Aspect ratio: 1:1 (must be a perfect square)
File format: JPG or PNG
Color space: sRGB
File size: Max 4MB

The song is called "Still, Can We Wander?"
The artist is "Milo Fenwright"

We have no images of Milo, so it really is open to imagination.

Target Market(s)

Wavelume listeners

Industry/Entity Type

Music

```html
<!DOCTYPE html>
<html lang="en">
<head>
<meta charset="utf-8">
<title>Still, Can We Wander? — Milo Fenwright</title>
<link rel="stylesheet" href="https://fonts.googleapis.com/css2?family=Cinzel+Decorative:wght@400;700&family=Cinzel:wght@500&family=Raleway:wght@300&display=swap">
<style>
  :root {
    --bg-deep: #07090c;
    --bg-mid: #111720;
    --title-cyan: #4fb4d0;
    --title-glow: rgba(40, 170, 230, 0.7);
    --artist-gold: #d9a46a;
    --art-cyan: rgba(60, 190, 230, 0.55);
    --art-cyan-soft: rgba(31, 111, 136, 0.45);
    --art-red: rgba(210, 60, 70, 0.5);
    --art-red-soft: rgba(122, 34, 48, 0.45);
    --art-floor: rgba(40, 50, 64, 0.6);
  }
  * { margin: 0; padding: 0; box-sizing: border-box; }
  html, body {
    width: 1200px;
    height: 1200px;
    overflow: hidden;
    background: var(--bg-deep);
  }
  .cover {
    position: relative;
    width: 1200px;
    height: 1200px;
    overflow: hidden;
    background: radial-gradient(ellipse at 50% 55%, var(--bg-mid) 0%, var(--bg-deep) 70%);
  }
  .title {
    position: absolute;
    left: 0;
    right: 0;
    top: 100px;
    text-align: center;
    font-family: "Cinzel Decorative", serif;
    font-weight: 400;
    color: var(--title-cyan);
    text-shadow: 0 0 10px var(--title-glow), 0 0 26px var(--title-glow);
    line-height: 1;
  }
  .title-line-small {
    display: block;
    font-size: 76px;
    letter-spacing: 1px;
  }
  .title-comma {
    font-family: "Cinzel", serif;
    font-weight: 500;
    margin-right: 0.18em;
  }
  .title-line-large {
    display: block;
    font-size: 122px;
    margin-top: 20px;
    letter-spacing: 1px;
  }
  .artwork {
    position: absolute;
    left: 330px;
    top: 420px;
    width: 540px;
    height: 560px;
    background:
      radial-gradient(ellipse 30% 38% at 38% 42%, var(--art-cyan) 0%, transparent 70%),
      radial-gradient(ellipse 30% 38% at 62% 42%, var(--art-red) 0%, transparent 70%),
      radial-gradient(ellipse 45% 55% at 33% 50%, var(--art-cyan-soft) 0%, transparent 75%),
      radial-gradient(ellipse 45% 55% at 67% 50%, var(--art-red-soft) 0%, transparent 75%),
      radial-gradient(ellipse 55% 12% at 50% 90%, var(--art-floor) 0%, transparent 100%);
  }
  .artist {
    position: absolute;
    left: 0;
    right: 0;
    top: 1044px;
    text-align: center;
    font-family: "Raleway", sans-serif;
    font-weight: 300;
    font-size: 48px;
    letter-spacing: 1px;
    color: var(--artist-gold);
  }
</style>
</head>
<body>
  <main class="cover">
    <h1 class="title">
      <span class="title-line-small">STILL<span class="title-comma">,</span>CAN WE</span>
      <span class="title-line-large">WANDER?</span>
    </h1>
    <div class="artwork" role="img" aria-label="Silhouettes of a man and a woman standing back to back on either side of a glowing neon heart split down the middle, cyan on his side and red on hers, reflected on a dark floor"></div>
    <p class="artist">MILO FENWRIGHT</p>
  </main>
</body>
</html>
```